2018 PLVWA Conference Theme Artwork

We need artwork designed around the theme of this year's human resources conference. The theme is "Celebrating 20 Years Together Towards Tomorrow". The artwork should be designed as a 4x6 postcard and will eventually be adapted/reformatted to use on the registration website, sales materials, e-newsletters, conference guide cover and signage.

Target Market(s)

Attendees are human resources professionals. Exhibitors and sponsors are companies who want to sell their products/services to human resource professionals

Colors

Designer to choose colors to be used in the design.

Requirements
Must have
• NO BORING PIXBANQ IMAGERY PLEASE.
• Theme: Celebrating 20 Years Together Towards Tomorrow
• Event: 20th Annual PLVW Conference
• Dates/Times: Tuesday, May 15, 2018, 12:30pm - 5:00pm and Wednesday, May 16, 2018 7:30am - 5:30pm
• Website: plvwsummit.example
• Location: The HALL at the Corvane Manchester
Nice to have
• Engaging, celebratory, visually attractive
Should not have
• NO BORING PIXBANQ IMAGERY.

```html
<!DOCTYPE html>
<html lang="en">
<head>
<meta charset="utf-8">
<title>20th Annual PLVW Conference Postcard</title>
<link rel="stylesheet" href="https://fonts.googleapis.com/css2?family=Roboto+Condensed:wght@300;400;700;900&display=swap">
<style>
  :root {
    --page-bg: #e4e4e4;
    --brand-blue: #064a86;
    --deep-navy: #0b2c4a;
    --ink: #111418;
    --white: #ffffff;
    --band-light: #ffffff;
    --band-shade: #e9e9e9;
    --art-red: #e2334b;
    --art-yellow: #f4c21d;
    --art-teal: #1fb0c9;
    --art-purple: #7a3e9d;
    --art-green: #3aaa55;
  }
  html, body {
    margin: 0;
    width: 1200px;
    height: 1200px;
    overflow: hidden;
    background: var(--page-bg);
    font-family: "Roboto Condensed", "Arial Narrow", sans-serif;
  }
  .postcard {
    position: absolute;
    left: 60px;
    top: 232px;
    width: 1080px;
    height: 736px;
    background: linear-gradient(90deg, var(--band-shade) 0%, var(--band-light) 45%, var(--band-shade) 100%);
    box-shadow: 0 6px 18px rgba(0,0,0,0.25);
    overflow: hidden;
  }
  .hero {
    position: absolute;
    left: 0;
    top: 0;
    width: 1080px;
    height: 508px;
  }
  .hero-text {
    position: absolute;
    right: 44px;
    top: 0;
    text-align: right;
    color: var(--white);
  }
  .hero-line {
    position: absolute;
    right: 0;
    white-space: nowrap;
    line-height: 1;
    letter-spacing: -0.5px;
  }
  .line-celebrating { top: 44px; font-size: 56px; font-weight: 400; }
  .line-years { top: 100px; font-size: 80px; font-weight: 400; }
  .line-together { top: 179px; font-size: 60px; font-weight: 700; }
  .line-tomorrow { top: 248px; font-size: 60px; font-weight: 700; }
  .line-annual { top: 364px; font-size: 62px; font-weight: 300; }
  .line-event { top: 434px; font-size: 62px; font-weight: 700; }

  .org-name {
    position: absolute;
    left: 36px;
    top: 500px;
    display: flex;
    align-items: center;
    gap: 12px;
    color: var(--brand-blue);
    font-size: 34px;
    font-weight: 700;
    letter-spacing: 0.5px;
  }
  .org-mark {
    width: 26px;
    height: 26px;
    background: var(--brand-blue);
  }
  .venue {
    position: absolute;
    left: 38px;
    top: 598px;
    display: flex;
    align-items: center;
    gap: 18px;
  }
  .venue-text {
    color: var(--ink);
    font-size: 27px;
    font-weight: 700;
    line-height: 34px;
    text-transform: uppercase;
  }
  .website {
    position: absolute;
    left: 114px;
    top: 682px;
    color: var(--brand-blue);
    font-size: 24px;
    font-weight: 700;
    line-height: 28px;
    letter-spacing: 0.3px;
  }
  .schedule {
    position: absolute;
    right: 40px;
    top: 534px;
    text-align: right;
    color: var(--ink);
    font-size: 27px;
    font-weight: 700;
    line-height: 34px;
  }
  .schedule p { margin: 0; }
  .schedule .day + .day { margin-top: 30px; }
</style>
</head>
<body>
  <main class="postcard">
    <svg class="hero" width="1080" height="508" viewBox="0 0 1080 508">
      <defs>
        <linearGradient id="crowdTones" x1="0" y1="0" x2="1" y2="1">
          <stop offset="0" stop-color="var(--art-red)"/>
          <stop offset="0.3" stop-color="var(--art-yellow)"/>
          <stop offset="0.55" stop-color="var(--art-teal)"/>
          <stop offset="0.8" stop-color="var(--art-purple)"/>
          <stop offset="1" stop-color="var(--art-green)"/>
        </linearGradient>
      </defs>
      <polygon class="crowd-art" role="img"
        aria-label="Illustration: a colourful crowd of small figures with a magnifying glass highlighting a pair of people"
        points="0,0 560,0 398,460 0,460" fill="url(#crowdTones)"/>
      <polygon class="fold-shadow" points="340,460 400,455 383,508" fill="var(--deep-navy)"/>
      <polygon class="title-panel" points="540,0 1080,0 1080,508 383,508" fill="var(--brand-blue)"/>
    </svg>

    <div class="hero-text">
      <div class="hero-line line-celebrating">CELEBRATING</div>
      <div class="hero-line line-years">20 YEARS</div>
      <div class="hero-line line-together">TOGETHER TOWARDS</div>
      <div class="hero-line line-tomorrow">TOMORROW</div>
      <div class="hero-line line-annual">20TH ANNUAL</div>
      <div class="hero-line line-event">PLVW CONFERENCE</div>
    </div>

    <div class="org-name"><span class="org-mark"></span>PLVWA COUNCIL</div>

    <div class="venue">
      <svg class="pin-icon" width="58" height="58" viewBox="0 0 58 58" aria-hidden="true">
        <circle cx="29" cy="29" r="29" fill="var(--brand-blue)"/>
        <path d="M29 12c-7 0-12 5-12 11.5C17 32 29 46 29 46s12-14 12-22.5C41 17 36 12 29 12z" fill="var(--white)"/>
        <circle cx="29" cy="23.5" r="4.5" fill="var(--brand-blue)"/>
      </svg>
      <div class="venue-text">The HALL at the<br>Corvane Manchester</div>
    </div>

    <div class="website">plvwsummit.example</div>

    <div class="schedule">
      <div class="day">
        <p>TUESDAY, MAY 15, 2018</p>
        <p>12:30PM - 5:00PM</p>
      </div>
      <div class="day">
        <p>WEDNESDAY, MAY 16, 2018</p>
        <p>7:30AM - 5:30PM</p>
      </div>
    </div>
  </main>
</body>
</html>
```